Business Card and Letterhead for Vantage Psychology

We need a business card design and letterhead to use for our Psychology firm that specializes in psychoeducational assessments and individual therapy. Our motto is Purpose-Driven Assessments, Meaning-Centered Therapy.Our contact information is as follows:
Vantage Psychology
The Marwick Block - 6127-48St.
Box 2716 Kestrel Ridge, SK
T2K 3M8
t 403.555.0148 (VANT)
f 403.555.0172
www.vantagepsychology-example.ca
The business card will be used for two different psychologists so I can supply names nearer to completion. We prefer clean, uncluttered looks.

Target Market(s)

Clients, Educators

Font styles to use
Sans Serif

Colors

Designer to choose colors to be used in the design.

Requirements
Must have
• All relevant contact info, logo, some "white" space.
Nice to have
• It would be nice to see letterhead options that have the logo on the top of the page but also options that have it on the side. I think top of the page is probably our preference.
Should not have
• Too much clutter!

```html
<!DOCTYPE html>
<html lang="en">
<head>
<meta charset="utf-8">
<title>Vantage Psychology – Stationery</title>
<link href="https://fonts.googleapis.com/css2?family=Lato:wght@400;700&display=swap" rel="stylesheet">
<style>
  :root {
    --bg: #a3a3a3;
    --brand-blue: #67bddd;
    --brand-orange: #f6a04d;
    --paper: #ffffff;
    --ink: #333333;
    --ink-soft: #555555;
    --faint: #f3f3f3;
    --window: #ececec;
  }
  * { box-sizing: border-box; margin: 0; padding: 0; }
  html, body { width: 1200px; height: 958px; overflow: hidden; }
  body { background: var(--bg); font-family: "Lato", sans-serif; color: var(--ink); position: relative; }

  .sheet { position: absolute; background: var(--paper); box-shadow: 8px 10px 18px rgba(0,0,0,.28); overflow: hidden; }
  .sheet--blue { background: var(--brand-blue); }

  .wordmark { display: flex; flex-direction: column; align-items: center; gap: 6px; }
  .wordmark__dot { border-radius: 50%; background: var(--brand-blue); }
  .wordmark__name { font-weight: 400; letter-spacing: .06em; text-transform: uppercase; color: var(--brand-blue); white-space: nowrap; }
  .sheet--blue .wordmark__dot { background: var(--paper); }
  .sheet--blue .wordmark__name { color: var(--paper); }

  /* business cards */
  .card { top: 38px; width: 211px; height: 121px; }
  .card--1 { left: 47px; } .card--2 { left: 341px; } .card--3 { left: 634px; } .card--4 { left: 928px; border-bottom: 3px solid var(--brand-blue); }
  .card .wordmark { position: absolute; left: 0; right: 0; top: 30px; }
  .card .wordmark__dot { width: 34px; height: 34px; }
  .card .wordmark__name { font-size: 10px; }
  .card__url { position: absolute; left: 0; right: 0; bottom: 10px; text-align: center; font-size: 6px; color: var(--ink-soft); }
  .sheet--blue .card__url { color: var(--paper); }
  .card--4 .wordmark { left: 4px; right: auto; width: 92px; top: 38px; }
  .card--4 .wordmark__dot { width: 24px; height: 24px; }
  .card--4 .wordmark__name { font-size: 6px; }
  .card__contact { position: absolute; left: 98px; top: 22px; padding-left: 8px; border-left: 1px solid var(--brand-blue); height: 78px; font-size: 5px; line-height: 1.35; color: var(--ink-soft); white-space: nowrap; }
  .card__name { font-size: 8.5px; color: var(--brand-blue); font-weight: 700; line-height: 1.1; }
  .card__role { margin-bottom: 5px; }
  .card__address { margin-bottom: 4px; }

  .icon-row { display: flex; align-items: center; gap: 4px; }
  .icon { flex: none; fill: var(--brand-blue); }

  /* letterhead */
  .letterhead { left: 45px; top: 196px; width: 500px; height: 708px; border-top: 3px solid var(--brand-blue); }
  .letterhead .wordmark { position: absolute; left: 40px; top: 36px; width: 175px; }
  .letterhead .wordmark__dot { width: 62px; height: 62px; }
  .letterhead .wordmark__name { font-size: 14px; }
  .letterhead__contact { position: absolute; left: 330px; top: 40px; padding-left: 10px; border-left: 1px solid #999; font-size: 7.2px; line-height: 1.3; color: var(--ink); white-space: nowrap; }
  .letterhead__contact .icon-row { gap: 6px; }
  .letterhead__address { margin-bottom: 3px; }
  .letterhead__body { position: absolute; left: 40px; top: 210px; width: 364px; font-size: 7.3px; line-height: 1.6; letter-spacing: .02em; color: var(--ink); }
  .letterhead__body p + p { margin-top: 11px; }
  .signature { position: absolute; left: 45px; top: 430px; width: 130px; height: 28px; background: linear-gradient(90deg, #ececec, #f6f6f6); }
  .faint-mark { position: absolute; border-radius: 50%; background: var(--faint); }
  .letterhead .faint-mark { left: 170px; top: 490px; width: 140px; height: 140px; }
  .footer-band { position: absolute; left: 0; right: 0; bottom: 0; height: 12px; background: var(--brand-blue); color: var(--paper); font-size: 7px; text-align: center; line-height: 12px; }

  /* envelopes */
  .envelope-back { left: 615px; top: 294px; width: 524px; height: 261px; }
  .envelope-back__flap { position: absolute; left: 0; top: 0; width: 524px; height: 78px; }
  .envelope-back .wordmark__dot { position: absolute; left: 247px; top: 26px; width: 30px; height: 30px; background: var(--paper); border-radius: 50%; }
  .envelope-back__address { position: absolute; left: 0; right: 0; top: 236px; text-align: center; font-size: 5.4px; color: var(--ink); }
  .envelope-back__address .sep { color: var(--brand-blue); }

  .envelope-front { left: 615px; top: 642px; width: 524px; height: 262px; }
  .envelope-front .wordmark { position: absolute; left: 34px; top: 22px; width: 160px; }
  .envelope-front .wordmark__dot { width: 48px; height: 48px; }
  .envelope-front .wordmark__name { font-size: 12px; }
  .envelope-front__window { position: absolute; left: 35px; top: 118px; width: 208px; height: 91px; background: var(--window); border: 1px solid #d6d6d6; border-radius: 3px; }
  .envelope-front .faint-mark { left: 317px; top: 78px; width: 116px; height: 116px; }
</style>
</head>
<body>

  <section class="sheet sheet--blue card card--1">
    <div class="wordmark"><span class="wordmark__dot"></span><span class="wordmark__name">Vantage Psychology</span></div>
    <p class="card__url">www.vantagepsychology-example.ca</p>
  </section>

  <section class="sheet sheet--blue card card--2">
    <div class="wordmark"><span class="wordmark__dot"></span><span class="wordmark__name">Vantage Psychology</span></div>
    <p class="card__url">www.vantagepsychology-example.ca</p>
  </section>

  <section class="sheet card card--3">
    <div class="wordmark"><span class="wordmark__dot"></span><span class="wordmark__name">Vantage Psychology</span></div>
    <p class="card__url">www.vantagepsychology-example.ca</p>
  </section>

  <section class="sheet card card--4">
    <div class="wordmark"><span class="wordmark__dot"></span><span class="wordmark__name">Vantage Psychology</span></div>
    <div class="card__contact">
      <p class="card__name">Daniel Ashford</p>
      <p class="card__role">Psychologist</p>
      <p class="card__address">Vantage Psychology<br>The Marwick Block - 6127-48St.<br>Box 2716 Kestrel Ridge, SK, T2K 3M8</p>
      <p class="icon-row"><svg class="icon" width="5" height="5" viewBox="0 0 10 10"><path d="M2 0l2 2.5-1.2 1.3a6 6 0 0 0 3.4 3.4L7.5 6 10 8l-1.5 2C4 10 0 6 0 1.5z"/></svg>403.555.0148 (VANT)</p>
      <p class="icon-row"><svg class="icon" width="5" height="5" viewBox="0 0 10 10"><rect x="2" y="0" width="6" height="3"/><rect x="0" y="3.5" width="10" height="4"/><rect x="2" y="8" width="6" height="2"/></svg>403.555.0172</p>
      <p class="icon-row"><svg class="icon" width="5" height="5" viewBox="0 0 10 10"><rect x="0" y="2" width="10" height="6"/></svg>info@vantagepsychology-example.ca</p>
      <p class="icon-row"><svg class="icon" width="5" height="5" viewBox="0 0 10 10"><circle cx="5" cy="5" r="5"/></svg>www.vantagepsychology-example.ca</p>
    </div>
  </section>

  <section class="sheet letterhead">
    <div class="wordmark"><span class="wordmark__dot"></span><span class="wordmark__name">Vantage Psychology</span></div>
    <div class="letterhead__contact">
      <p class="letterhead__address">Vantage Psychology<br>The Marwick Block - 6127-48St.<br>Box 2716 Kestrel Ridge, SK, T2K 3M8</p>
      <p class="icon-row"><svg class="icon" width="6" height="6" viewBox="0 0 10 10"><path d="M2 0l2 2.5-1.2 1.3a6 6 0 0 0 3.4 3.4L7.5 6 10 8l-1.5 2C4 10 0 6 0 1.5z"/></svg>403.555.0148 (VANT)</p>
      <p class="icon-row"><svg class="icon" width="6" height="6" viewBox="0 0 10 10"><rect x="2" y="0" width="6" height="3"/><rect x="0" y="3.5" width="10" height="4"/><rect x="2" y="8" width="6" height="2"/></svg>403.555.0172</p>
      <p class="icon-row"><svg class="icon" width="6" height="6" viewBox="0 0 10 10"><rect x="0" y="2" width="10" height="6"/></svg>info@vantagepsychology-example.ca</p>
    </div>
    <div class="letterhead__body">
      <p>Lorem ipsum dolor sit amet, consectetur adipiscing elit. Praesent non est diam. Vivamus risus sem, gravida sit amet nibh ut, ornare lobortis ante. Aliquam sollicitudin, mauris tincidunt semper venenatis, orci est pretium augue, ut vestibulum felis velit bibendum urna. Integer sollicitudin aliquet ligula, non ultricies nisl efficitur nec. Aliquam felis lorem, facilisis ac condimentum quis, consectetur volutpat lacus. Proin fermentum sem quis elit efficitur, eu tempus magna maximus.</p>
      <p>Aenean a mi tortor. Morbi pretium mi sed cursus vehicula. Lorem ipsum dolor sit amet, consectetur adipiscing elit. In finibus eros ac maximus finibus. Nunc pretium pellentesque tellus. Nullam accumsan nisl non diam camodo sagittis. Nunc et ante sit amet urna auctor convallis. Maecenas sed fringilla metus, sit amet vulputate felis. Morbi eget tempor nisi. Aliquam erat volutpat. Aenean laoreet interdum tempus.</p>
      <p>Maecenas dignissim placerat mauris, vitae sollicitudin ex. Integer bibendum maximus mauris, ac tempor urna viverra id. Integer tincidunt lobortis nisl at posuere. Sed faucibus vulputate finibus. Maecenas convallis, sem quis pellentesque cursus, urna quam aliquam augue, quis porttitor eros est nec lectus. Sed mattis at tellus ut blandit. Aenean nunc magna, viverra sed mauris vel, porta finibus lacus. Nullam bibendum turpis rutrum porta placerat</p>
    </div>
    <div class="signature" role="img" aria-label="Handwritten signature of Neil Harper"></div>
    <span class="faint-mark"></span>
    <p class="footer-band">www.vantagepsychology-example.ca</p>
  </section>

  <section class="sheet envelope-back">
    <svg class="envelope-back__flap" viewBox="0 0 524 78" aria-hidden="true">
      <path d="M0 0H524L500 68Q497 76 488 76H36Q27 76 24 68Z" fill="var(--brand-blue)"/>
    </svg>
    <span class="wordmark__dot"></span>
    <p class="envelope-back__address">Vantage Psychology <span class="sep">•</span> The Marwick Block - 6127-48St. <span class="sep">•</span> Box 2716 Kestrel Ridge <span class="sep">•</span> SK, T2K 3M8</p>
  </section>

  <section class="sheet envelope-front">
    <div class="wordmark"><span class="wordmark__dot"></span><span class="wordmark__name">Vantage Psychology</span></div>
    <div class="envelope-front__window"></div>
    <span class="faint-mark"></span>
    <p class="footer-band">www.vantagepsychology-example.ca</p>
  </section>

</body>
</html>
```